Business Card Design

I need a business card and logo for a new company based in Manhattan, Kansas called "Bright Ladder, LLC". I am a project management consultant. I specialize in laying the foundation for businesses and business owners to get their projects on track. Think of it as if you were wanting to go from coast to coast on a train. Before you can jump on the train and sell tickets, you have to design the path the train will take, acquire the land, clear the trees, level the ground, prepare the base for the track, lay the track and finally place the train on the track (That's what I do with my clients). Once the train is on the track and I've provided them with the operations manual, then they and their managers get to drive the train. I don't have color preferences. The final design should communicate a clear direction or path to growing the customer's business.
Updates

Since I am in need of a logo as well, I have also created a logo design project that will work in conjunction with this project.

Project Deadline Extended
Reason: Accepted a company logo this afternoon that I would like to have cards designed around. Sorry for jumping the gun and posting both projects at the same time.

Industry/Entity Type

Business

Contact Information for Business Card

Owner: Dale Perrin. Business Name: Bright Ladder, LLC. Business Address: 4871 Maplewood Lane, Larkhaven, ZZ, 00000. Business Phone Number: 555-640-1759. Business Email: dale@brightladderllc.example

```html
<!DOCTYPE html>
<html lang="en">
<head>
<meta charset="utf-8">
<title>Bright Ladder, LLC — Business Card</title>
<link rel="stylesheet" href="https://fonts.googleapis.com/css2?family=Arimo:wght@400&display=swap">
<style>
  :root {
    --page-bg: #e9e9ea;
    --card-bg: #0b0b0b;
    --ink: #ffffff;
    --accent-disc: #3a3a3a;
  }
  * { margin: 0; padding: 0; box-sizing: border-box; }
  html, body {
    width: 1200px;
    height: 864px;
    overflow: hidden;
    background: var(--page-bg);
    font-family: "Arimo", Arial, sans-serif;
  }
  .card {
    position: absolute;
    left: 100px;
    top: 146px;
    width: 1000px;
    height: 572px;
    background: var(--card-bg);
    overflow: hidden;
    color: var(--ink);
  }
  .card__disc {
    position: absolute;
    left: 700px;
    top: 150px;
    width: 420px;
    height: 420px;
    border-radius: 50%;
    background: var(--accent-disc);
    opacity: 0.55;
  }
  .brand {
    position: absolute;
    left: 190px;
    top: 52px;
    width: 300px;
    text-align: center;
  }
  .brand__mark {
    display: block;
    width: 70px;
    height: 70px;
    margin: 0 auto 20px;
    border-radius: 50%;
    background: var(--ink);
  }
  .brand__name {
    font-size: 34px;
    font-variant: small-caps;
    letter-spacing: 1px;
    white-space: nowrap;
  }
  .owner {
    position: absolute;
    right: 120px;
    top: 62px;
    font-size: 34px;
  }
  .contacts {
    position: absolute;
    left: 96px;
    top: 318px;
    list-style: none;
  }
  .contacts__item {
    display: flex;
    align-items: flex-start;
    font-size: 26px;
    line-height: 32px;
    margin-bottom: 20px;
    white-space: nowrap;
  }
  .contacts__icon {
    flex: 0 0 26px;
    height: 32px;
    margin-right: 36px;
    fill: var(--ink);
  }
</style>
</head>
<body>
  <article class="card">
    <div class="card__disc" role="img" aria-label="Large faint brand emblem decoration"></div>

    <header class="brand">
      <span class="brand__mark"></span>
      <div class="brand__name">Bright Ladder, LLC</div>
    </header>

    <div class="owner">Dale Perrin</div>

    <ul class="contacts">
      <li class="contacts__item">
        <svg class="contacts__icon" viewBox="0 0 26 32" aria-hidden="true">
          <path d="M6 5c2-1 3 0 4 3l1 3c0 1-1 2-2 3 1 3 3 6 6 8 1-1 2-2 3-1l3 2c2 1 2 2 1 4l-2 2c-8 0-16-10-16-20z"/>
        </svg>
        <span>555-640-1759</span>
      </li>
      <li class="contacts__item">
        <svg class="contacts__icon" viewBox="0 0 26 32" aria-hidden="true">
          <path d="M13 4a8 8 0 0 0-8 8c0 6 8 16 8 16s8-10 8-16a8 8 0 0 0-8-8zm0 11a3 3 0 1 1 0-6 3 3 0 0 1 0 6z"/>
        </svg>
        <span>4871 Maplewood Lane,<br>Larkhaven, ZZ, 00000</span>
      </li>
      <li class="contacts__item">
        <svg class="contacts__icon" viewBox="0 0 26 32" aria-hidden="true">
          <path d="M1 9h24v15H1z M2.5 10.5 13 18l10.5-7.5" fill="none" stroke="#fff" stroke-width="2"/>
        </svg>
        <span>dale@brightladderllc.example</span>
      </li>
    </ul>
  </article>
</body>
</html>
```